RK Cooling (logo) - Celebrating 55 Years Servicing the Chicago Suburbs. Summer is Almost Here! Make sure your system is running properly and efficiently. The industry standard recommends an A/C Clean & Check once a year.
A/C Clean & Check
Regular Preventive Maintenance Can:
-Help Prolong the Life of your Equipment
-Help Lower Your Monthly Energy Costs
-Save Costs on Future Repairs

Mention this Postcard and Take $10.00 Off
Call (555) 384-9120 I Address: 718 Birchwood Ave. Marvale, IL
_______________________________________________
BACK SIDE:
Proudly Serving Chicagoland Area Since 1961- We Also Service and Sell:
-Coastline Prime Equipment.
-Brightvane Air Cleaners & Humidifier Systems.
-Hot Water Heaters, Boilers, and Digital Thermostats.
-Residential and Commercial Fabrication. Custom Welding.

Schedule Your Spring Clean & Check Today
Phone: (555) 384-9120
Mail: rkcooling@mailnest.example
Website: www.rkcoolingair.example

I had pixel guild make a Fall Clean and Check (for furnaces) in September of 2015. Feel free too look back for ideas. The postcard needs to be creative and not the same as the fall one! Added Tuesday, March 29, 2016

Target Market(s)

HVAC Industry, Residential

Industry/Entity Type

Air Conditioning

Colors
0255a3
f6faec

Requirements
Must have
• The following text in the project description. Feel free to add more.
Nice to have
• One small picture or clipart on the front. Maybe a picture of something summery or an air conditioner.
Should not have
• No spelling mistakes. Nothing too basic.

```html
<!DOCTYPE html>
<html lang="en">
<head>
<meta charset="utf-8">
<title>RK Cooling – Spring Clean &amp; Check Postcard</title>
<link rel="stylesheet" href="https://fonts.googleapis.com/css2?family=Anton&family=Lato:ital,wght@0,400;0,700;0,900;1,400&display=swap">
<style>
  :root {
    --blue: #0255a3;
    --blue-dark: #013f7c;
    --blue-light: #2f7fcf;
    --cream: #f6faec;
    --red: #e8262b;
    --ink: #3d3d3d;
    --white: #ffffff;
    --stamp: #d3d3d3;
    --backdrop: #dcdcdc;
  }
  * { box-sizing: border-box; margin: 0; padding: 0; }
  html, body { width: 825px; height: 1200px; overflow: hidden; }
  body { background: var(--backdrop); font-family: "Lato", sans-serif; position: relative; }

  .postcard { position: absolute; left: 93px; width: 642px; background: var(--white); overflow: hidden; box-shadow: 0 2px 6px rgba(0,0,0,.25); }
  .postcard--front { top: 73px; height: 497px; }
  .postcard--back { top: 630px; height: 495px; }
  .shapes { position: absolute; inset: 0; }
  .abs { position: absolute; }
  .headline { font-family: "Anton", sans-serif; font-weight: 400; letter-spacing: .3px; }

  /* call badge */
  .call-badge { position: absolute; border-radius: 50%; border: 4px solid var(--white);
    background: radial-gradient(circle at 35% 30%, var(--blue-light), var(--blue) 60%, var(--blue-dark));
    box-shadow: 0 3px 8px rgba(0,0,0,.35); color: var(--white); text-align: center;
    display: flex; flex-direction: column; justify-content: center; align-items: center; }
  .call-badge__word { font-family: "Anton", sans-serif; line-height: 1; }
  .call-badge__phone { font-weight: 700; font-size: 9px; margin-top: 3px; }

  /* front */
  .product-photo { left: 24px; top: 32px; width: 262px; height: 158px; border-radius: 4px;
    background: linear-gradient(135deg, #f2f4f6, #c9d0d8 60%, #e8ebee); }
  .brand { left: 352px; top: 42px; display: flex; align-items: center; gap: 8px; }
  .brand__dot { width: 18px; height: 18px; border-radius: 50%; background: var(--blue-dark); }
  .brand__name { font-family: "Anton", sans-serif; font-size: 34px; color: var(--blue-dark); line-height: 1; }

  .anniversary { left: 336px; top: 178px; width: 290px; text-align: center; color: var(--white); text-shadow: 1px 1px 2px rgba(0,0,0,.35); }
  .anniversary__big { font-size: 27px; line-height: 1.1; }
  .anniversary__small { font-size: 18px; line-height: 1.1; }

  .offer { left: 20px; top: 258px; width: 220px; text-align: center; }
  .offer__lead { font-size: 19px; color: var(--blue); }
  .offer__take { font-size: 76px; color: var(--ink); line-height: 1; margin-top: 2px; }
  .offer__amount { font-size: 38px; color: var(--blue); line-height: 1; margin-top: 2px; }

  .summer { right: 30px; top: 295px; width: 300px; text-align: right; color: var(--white); }
  .summer__title { font-weight: 900; font-size: 19px; }
  .summer__copy { font-size: 11.5px; line-height: 1.3; margin-top: 10px; }
  .benefits { list-style: none; margin-top: 10px; font-style: italic; font-size: 12.5px; line-height: 1.4; }
  .benefits li::after { content: ""; display: inline-block; width: 6px; height: 6px; border-radius: 50%; background: var(--red); margin-left: 8px; vertical-align: middle; }

  .footer-bar { left: 0; right: 0; bottom: 0; height: 36px; background: var(--red); color: var(--white);
    font-size: 16.5px; letter-spacing: 1.6px; font-weight: 700; display: flex; align-items: center; padding-left: 32px; }

  /* back */
  .services { left: 25px; top: 20px; width: 320px; }
  .services__title { font-size: 16px; color: var(--blue); line-height: 1.25; }
  .services__sub { font-size: 16px; color: var(--ink); line-height: 1.25; }
  .services__list { list-style: none; margin-top: 8px; font-size: 10.5px; color: var(--ink); line-height: 1.4; }
  .services__list li::before { content: ""; display: inline-block; width: 5px; height: 5px; border-radius: 50%; background: var(--red); margin-right: 10px; vertical-align: middle; }

  .schedule { left: 30px; top: 186px; color: var(--white); text-shadow: 1px 1px 2px rgba(0,0,0,.35); }
  .schedule__big { font-size: 35px; line-height: 1.05; }
  .schedule__small { font-size: 19px; line-height: 1.1; }

  .contact { left: 33px; top: 302px; color: var(--white); font-weight: 700; font-size: 15.5px; line-height: 1.7; }

  .stamp-box { left: 546px; top: 28px; width: 66px; height: 66px; background: var(--stamp); }
  .address-area { left: 82px; top: 408px; width: 560px; height: 87px; background: var(--white); }
</style>
</head>
<body>

<!-- FRONT -->
<section class="postcard postcard--front">
  <svg class="shapes" width="642" height="497" viewBox="0 0 642 497">
    <defs>
      <linearGradient id="frontBlue" x1="0" x2="1">
        <stop offset="0" stop-color="#01468a"/><stop offset=".6" stop-color="#1e6fc0"/><stop offset="1" stop-color="#01468a"/>
      </linearGradient>
    </defs>
    <!-- left cream offer panel -->
    <rect x="0" y="220" width="320" height="232" fill="var(--cream)"/>
    <rect x="0" y="207" width="300" height="11" fill="var(--red)"/>
    <!-- right side panels -->
    <polygon points="310,0 642,0 642,127 294,127" fill="var(--cream)"/>
    <polygon points="294,127 642,127 642,138 292,138" fill="var(--blue)"/>
    <polygon points="290,142 642,142 642,277 281,277" fill="var(--red)"/>
    <polygon points="284,284 642,284 642,452 316,452" fill="url(#frontBlue)"/>
    <!-- diagonal red edge stroke -->
    <polyline points="302,0 283,142 276,207 306,452" fill="none" stroke="var(--red)" stroke-width="6"/>
  </svg>

  <div class="abs product-photo" role="img" aria-label="Photo of an outdoor air conditioner unit with a wall-mounted indoor unit"></div>

  <div class="abs brand">
    <span class="brand__dot"></span>
    <span class="brand__name">RK Cooling</span>
  </div>

  <div class="call-badge" style="left:210px; top:156px; width:98px; height:98px;">
    <span class="call-badge__word" style="font-size:36px;">Call</span>
    <span class="call-badge__phone">(555) 384-9120</span>
  </div>

  <div class="abs anniversary headline">
    <div class="anniversary__big">Celebrating 55 Years</div>
    <div class="anniversary__small">Servicing the Chicago Suburbs</div>
  </div>

  <div class="abs offer headline">
    <div class="offer__lead">Mention this Postcard</div>
    <div class="offer__take">TAKE</div>
    <div class="offer__amount">$10.00 OFF</div>
  </div>

  <div class="abs summer">
    <div class="summer__title">Summer is Almost Here!</div>
    <p class="summer__copy">Make sure your system is running properly and efficiently. The industry standard recommends an A/C Clean &amp; Check once a year.</p>
    <ul class="benefits">
      <li>Help Prolong the Life of your Equipment</li>
      <li>Help Lower Your Monthly Energy Costs</li>
      <li>Save Costs on Future Repairs</li>
    </ul>
  </div>

  <div class="abs footer-bar">Call - (555) 384-9120 I Address: 718 Birchwood Ave. Marvale, IL</div>
</section>

<!-- BACK -->
<section class="postcard postcard--back">
  <svg class="shapes" width="642" height="495" viewBox="0 0 642 495">
    <defs>
      <linearGradient id="backBlue" x1="0" x2="1">
        <stop offset="0" stop-color="#01468a"/><stop offset=".55" stop-color="#1e6fc0"/><stop offset="1" stop-color="#01468a"/>
      </linearGradient>
    </defs>
    <polygon points="0,0 318,0 352,120 0,120" fill="var(--cream)"/>
    <polygon points="0,148 360,148 363,158 0,158" fill="var(--blue)"/>
    <polygon points="0,163 366,163 372,275 0,275" fill="var(--red)"/>
    <polygon points="0,275 372,275 352,408 82,408 82,495 0,495" fill="url(#backBlue)"/>
    <polyline points="325,0 362,150 380,275 360,408" fill="none" stroke="var(--red)" stroke-width="6"/>
    <rect x="82" y="408" width="560" height="87" fill="var(--white)"/>
  </svg>

  <div class="abs stamp-box"></div>

  <div class="abs services">
    <div class="services__title headline">Proudly Serving Chicagoland Area</div>
    <div class="services__sub headline">Since 1961- We Also Service and Sell:</div>
    <ul class="services__list">
      <li>Coastline Prime Equipment.</li>
      <li>Brightvane Air Cleaners &amp; Humidifier Systems.</li>
      <li>Hot Water Heaters, Boilers, and Digital Thermostats.</li>
      <li>Residential and Commercial Fabrication. Custom Welding.</li>
    </ul>
  </div>

  <div class="abs schedule headline">
    <div class="schedule__big">Schedule Your</div>
    <div class="schedule__small">Spring Clean &amp; Check Today</div>
  </div>

  <div class="call-badge" style="left:286px; top:162px; width:112px; height:112px;">
    <span class="call-badge__word" style="font-size:40px;">Call</span>
    <span class="call-badge__phone">(555) 384-9120</span>
  </div>

  <div class="abs contact">
    <div>Contact information:</div>
    <div>Mail: rkcooling@mailnest.example</div>
    <div>Website: www.rkcoolingair.example</div>
  </div>
</section>

</body>
</html>
```